Adventurous female pilot

I am looking for a personal business card, for a very well qualified female pilot, with a lot of aviation experience.

Currently an airline pilot, have worked as a bush pilot in Africa, looking to get into corporate aviation, or private jet owners.
Want a classy looking card for networking...

Could be interested in a retro\vintage look also?!

An idea,, is an african sunset background, with my wings\logo on it
Updates

I just want to say thank you to all of your for your amazing designs!

I have been very busy flying this past week , so not had a chance to be on the computer much.
But I provide some feedback, and conclusions very soon!
Thank you again.

Marla

Reason: Still waiting on a couple of revisions to be 100% about my choice!

Target Market(s)

corporate aviation, private jet owners, casino's,
General audience.
networking

Industry/Entity Type

Airline

Requirements
Nice to have
• Classy, edgy, sexy, but also feminine

```html
<!DOCTYPE html>
<html lang="en">
<head>
<meta charset="utf-8">
<title>Marla Hollis – Pilot Business Card</title>
<link rel="stylesheet" href="https://fonts.googleapis.com/css2?family=Yellowtail&family=Roboto+Slab:wght@400;700&family=Domine:wght@400&display=swap">
<style>
  :root {
    --backdrop: #e9e4dc;
    --card-cream: #f0eedf;
    --card-cream-shade: #e4e1c9;
    --ink-brown: #6a3a1c;
    --card-brown: #5a3318;
    --cream-text: #ecdcb8;
    --sketch-light: #e6dcc4;
    --sketch-mid: #c9ae8a;
  }
  * { box-sizing: border-box; margin: 0; padding: 0; }
  html, body {
    width: 1200px; height: 880px; overflow: hidden;
    background: var(--backdrop);
  }
  .canvas {
    width: 1200px; height: 880px;
    display: flex; align-items: center; justify-content: center; gap: 40px;
  }
  .card {
    width: 540px; height: 310px; position: relative; overflow: hidden;
    box-shadow: 0 6px 18px rgba(60, 35, 15, 0.18);
  }

  /* Front */
  .card-front { background: linear-gradient(135deg, var(--card-cream-shade), var(--card-cream) 55%); }
  .aviator-illustration {
    position: absolute; left: 22px; top: 20px; width: 245px; height: 270px;
  }
  .front-identity {
    position: absolute; left: 278px; top: 110px; width: 240px; text-align: center;
    color: var(--ink-brown);
  }
  .front-name {
    font-family: "Yellowtail", cursive; font-size: 44px; line-height: 1;
  }
  .front-rule { height: 2px; background: var(--ink-brown); margin: 6px 8px 6px; }
  .front-title {
    font-family: "Domine", serif; font-size: 20px; letter-spacing: 7px;
    padding-left: 7px;
  }

  /* Back */
  .card-back { background: var(--card-brown); color: var(--cream-text); }
  .back-header {
    position: absolute; left: 40px; right: 40px; top: 62px;
    display: flex; align-items: center; gap: 18px;
  }
  .header-rule { flex: 1; height: 1.5px; background: var(--cream-text); }
  .back-name {
    font-family: "Yellowtail", cursive; font-size: 40px; line-height: 1;
  }
  .contact-list {
    position: absolute; left: 40px; top: 150px;
    display: grid; grid-template-columns: 108px auto; row-gap: 12px;
    font-size: 17px;
  }
  .contact-label { font-family: "Roboto Slab", serif; font-weight: 700; }
  .contact-value { font-family: "Domine", serif; }
</style>
</head>
<body>
<main class="canvas">
  <section class="card card-front">
    <svg class="aviator-illustration" viewBox="0 0 245 270" role="img"
         aria-label="Sepia pen sketch of a vintage aviator in flight suit and leather cap standing beside a propeller plane wheel">
      <defs>
        <radialGradient id="sketchTone" cx="45%" cy="50%" r="65%">
          <stop offset="0%" stop-color="var(--sketch-mid)"/>
          <stop offset="100%" stop-color="var(--sketch-light)" stop-opacity="0"/>
        </radialGradient>
      </defs>
      <rect width="245" height="270" fill="url(#sketchTone)"/>
    </svg>
    <div class="front-identity">
      <h1 class="front-name">Marla Hollis</h1>
      <div class="front-rule"></div>
      <p class="front-title">PILOT</p>
    </div>
  </section>

  <section class="card card-back">
    <div class="back-header">
      <span class="header-rule"></span>
      <h2 class="back-name">Marla Hollis</h2>
      <span class="header-rule"></span>
    </div>
    <dl class="contact-list">
      <dt class="contact-label">Email</dt>
      <dd class="contact-value">: marlachollis@skymail.com</dd>
      <dt class="contact-label">Cell US</dt>
      <dd class="contact-value">: +1 702-555-0143</dd>
      <dt class="contact-label">Cell Taipei</dt>
      <dd class="contact-value">: +886 912-345-678</dd>
    </dl>
  </section>
</main>
</body>
</html>
```